Personal training poster - 1200X900mm

Poster to promote my new personal training service at my gym. The poster will be printed and put into an aframe to be seen by people walking past my gym. It needs to be simple and eye catching with the text i have put in the must haves. The text and image should be the prominent parts of the design.

Target Market(s)

30-50 year old females

Industry/Entity Type

Fitness

Font styles to use
Sans Serif

Requirements
Must have
• my logo
• exercise graphic
• Must include the following text:
• Are you looking for a personal trainer? Our expert trainers can help you achieve you take your health and fitness back!
• Contact details:
• 1300452908
• info@brightmotiongym.example.com.au
• Located under the Harbourside Club

```html
<!DOCTYPE html>
<html lang="en">
<head>
<meta charset="utf-8">
<title>Personal Training Poster – Bright Motion Gym</title>
<link rel="stylesheet" href="https://fonts.googleapis.com/css2?family=Alfa+Slab+One&family=Anton&family=Arvo:wght@400;700&family=Exo+2:wght@500;700&display=swap">
<style>
  :root {
    --ink: #121212;
    --backdrop: #181818;
    --photo-light: #8a8a8a;
    --photo-mid: #4a4a4a;
    --photo-dark: #262626;
    --yellow: #fcd22a;
    --brush-red: #8e0d0b;
    --signal-red: #e0211c;
    --white: #ffffff;
    --logo-blue: #1f6fd6;
  }
  * { margin: 0; padding: 0; box-sizing: border-box; }
  html, body { width: 988px; height: 1200px; overflow: hidden; background: var(--ink); }
  .poster { position: relative; width: 988px; height: 1200px; overflow: hidden; background: var(--backdrop); }

  .photo-woman {
    position: absolute; left: 540px; top: 0; width: 448px; height: 780px;
    background: linear-gradient(200deg, var(--photo-light) 0%, var(--photo-mid) 45%, var(--photo-dark) 80%, var(--backdrop) 100%);
    border-bottom-left-radius: 220px 360px;
    border-top-left-radius: 200px 300px;
  }
  .photo-man {
    position: absolute; left: 640px; top: 780px; width: 348px; height: 300px;
    background: linear-gradient(160deg, var(--photo-mid) 0%, var(--photo-dark) 60%, var(--backdrop) 100%);
    border-top-left-radius: 180px 160px;
  }
  .photo-trainer {
    position: absolute; left: 0; top: 520px; width: 130px; height: 300px;
    background: linear-gradient(90deg, var(--photo-dark) 0%, var(--backdrop) 100%);
    border-top-right-radius: 90px 140px;
    border-bottom-right-radius: 90px 140px;
  }

  .headline-are-you {
    position: absolute; left: 61px; top: 40px;
    font: 400 84px/1 "Alfa Slab One", serif; color: var(--yellow); white-space: nowrap;
  }
  .headline-looking {
    position: absolute; left: 64px; top: 108px;
    font: 400 132px/1 "Anton", sans-serif; color: var(--white); letter-spacing: 19px; white-space: nowrap;
  }
  .brush-band {
    position: absolute; left: 31px; top: 244px; width: 610px; height: 238px;
    background: var(--brush-red);
  }
  .headline-for-a {
    position: absolute; left: 110px; top: 364px;
    transform: translate(-50%, -50%) rotate(-90deg);
    font: 400 58px/1 "Alfa Slab One", serif; color: var(--yellow); white-space: nowrap;
  }
  .headline-pers, .headline-onal {
    position: absolute; left: 150px;
    font: 400 156px/1 "Alfa Slab One", serif; color: var(--yellow); white-space: nowrap;
  }
  .headline-pers { top: 222px; }
  .headline-onal { top: 334px; }
  .headline-trainer {
    position: absolute; left: 68px; top: 484px;
    font: 400 97px/1 "Alfa Slab One", serif; color: var(--white); white-space: nowrap;
  }

  .pitch {
    position: absolute; left: 95px; top: 611px;
    font: 500 45px/49px "Exo 2", sans-serif; color: var(--white); white-space: nowrap;
  }
  .pitch-lead { color: var(--yellow); }

  .brand {
    position: absolute; left: 282px; top: 800px; width: 470px; text-align: center;
  }
  .brand-dot {
    width: 150px; height: 150px; border-radius: 50%;
    background: var(--logo-blue); margin: 0 auto 40px;
  }
  .brand-name {
    font: 700 40px/1 "Exo 2", sans-serif; color: var(--yellow); letter-spacing: 2px; white-space: nowrap;
  }

  .contact-band { position: absolute; left: 0; top: 1070px; width: 988px; height: 130px; }
  .contact-phone { position: absolute; left: 40px; top: 1114px; display: flex; align-items: center; gap: 10px; }
  .contact-label { font: 700 19px/1 "Arvo", serif; color: var(--ink); }
  .contact-number { font: 700 50px/1 "Arvo", serif; color: var(--ink); letter-spacing: -2px; white-space: nowrap; }
  .contact-mail { position: absolute; left: 520px; top: 1124px; display: flex; gap: 10px; }
  .contact-email { font: 700 18px/1.25 "Arvo", serif; color: var(--ink); white-space: nowrap; }
  .contact-location { font: 400 19px/1.35 "Arvo", serif; color: var(--ink); white-space: nowrap; }
</style>
</head>
<body>
<main class="poster">
  <div class="photo-woman" role="img" aria-label="Black and white photo of a woman in a sports top lifting a dumbbell"></div>
  <div class="photo-man" role="img" aria-label="Black and white photo of a muscular man training low to the ground"></div>
  <div class="photo-trainer" role="img" aria-label="Dim photo of a trainer doing push-ups in the smoke"></div>

  <div class="brush-band"></div>
  <div class="headline-are-you">ARE YOU</div>
  <div class="headline-looking">LOOKING</div>
  <div class="headline-for-a">FOR A</div>
  <div class="headline-pers">PERS</div>
  <div class="headline-onal">ONAL</div>
  <div class="headline-trainer">TRAINER?</div>

  <p class="pitch">
    <span class="pitch-lead">Our expert trainers can</span><br>
    help you achieve you take<br>
    your health and fitness back!
  </p>

  <div class="brand">
    <div class="brand-dot"></div>
    <div class="brand-name">BRIGHT MOTION GYM</div>
  </div>

  <svg class="contact-band" viewBox="0 0 988 130" aria-hidden="true">
    <polygon fill="var(--yellow)" points="0,22 60,14 140,20 230,8 330,16 420,6 520,14 620,4 720,12 820,2 900,10 988,0 988,130 0,130"/>
  </svg>

  <div class="contact-phone">
    <svg width="66" height="66" viewBox="0 0 62 64" aria-hidden="true">
      <rect x="10" y="2" width="50" height="60" rx="6" fill="var(--signal-red)"/>
      <rect x="2" y="12" width="10" height="6" fill="var(--signal-red)"/>
      <rect x="2" y="29" width="10" height="6" fill="var(--signal-red)"/>
      <rect x="2" y="46" width="10" height="6" fill="var(--signal-red)"/>
      <path d="M26 14c3 0 5 6 4 8l-3 3c2 5 6 9 11 11l3-3c2-1 8 1 8 4l-2 6c-2 2-8 3-16-4s-11-15-9-20z" fill="var(--yellow)"/>
    </svg>
    <div>
      <div class="contact-label">Contact Us :</div>
      <div class="contact-number">1300 452 908</div>
    </div>
  </div>

  <div class="contact-mail">
    <svg width="30" height="22" viewBox="0 0 30 22" aria-hidden="true" style="margin-top:1px">
      <rect x="1" y="1" width="28" height="20" fill="var(--signal-red)"/>
      <path d="M1 1l14 11L29 1" fill="none" stroke="var(--yellow)" stroke-width="2"/>
    </svg>
    <div>
      <div class="contact-email">info@brightmotiongym.example.com.au</div>
      <div class="contact-location">Located under the Harbourside Club</div>
    </div>
  </div>
</main>
</body>
</html>
```